On going F&B business needs a new stationery design for festive occasion

Would like something like the attached file, but with a new look. The basis colours should still be green and yellow.

```html
<!DOCTYPE html>
<html lang="en">
<head>
<meta charset="utf-8">
<title>Bayan Eating House – Business Card</title>
<link href="https://fonts.googleapis.com/css2?family=Montserrat:wght@700&family=Roboto:wght@400;500&display=swap" rel="stylesheet">
<style>
  :root {
    --bg: #e9e8e6;
    --green: #0a4a22;
    --green-soft: #115a2c;
    --yellow: #e4e33a;
    --white: #f7f7f6;
    --ink: #333;
  }
  * { box-sizing: border-box; margin: 0; padding: 0; }
  html, body { width: 1200px; height: 959px; overflow: hidden; background: var(--bg); }
  body { position: relative; font-family: "Roboto", sans-serif; }

  .card {
    position: absolute;
    left: 232px;
    width: 736px;
    height: 420px;
    border-radius: 4px;
    box-shadow: 0 6px 18px rgba(0,0,0,.12);
    overflow: hidden;
  }
  .card--front { top: 40px; background: var(--green); }
  .card--back { top: 499px; background: var(--white); }

  .front__halo {
    position: absolute;
    right: 70px; top: 40px;
    width: 270px; height: 270px;
    border-radius: 50%;
    background: var(--green-soft);
    opacity: .55;
  }
  .brand {
    position: absolute;
    display: flex;
    align-items: center;
    gap: 14px;
    font-family: "Montserrat", sans-serif;
    font-weight: 700;
    text-transform: uppercase;
    line-height: 1.05;
  }
  .brand__dot { border-radius: 50%; flex: none; }
  .front__brand { left: 190px; top: 160px; color: var(--yellow); font-size: 38px; }
  .front__brand .brand__dot { width: 70px; height: 70px; background: var(--yellow); }
  .brand__sub { display: block; font-size: .62em; letter-spacing: .04em; }

  .back__brand { left: 52px; top: 150px; color: var(--green); font-size: 26px; }
  .back__brand .brand__dot { width: 52px; height: 52px; background: var(--green); }
  .back__divider {
    position: absolute; left: 360px; top: 80px;
    width: 2px; height: 150px; background: var(--green);
  }
  .contact { position: absolute; left: 392px; top: 78px; color: var(--ink); }
  .contact__name {
    font-family: "Montserrat", sans-serif; font-weight: 700;
    color: var(--green); font-size: 24px; text-transform: uppercase;
  }
  .contact__role { font-weight: 500; font-size: 17px; color: #444; margin-bottom: 10px; }
  .contact__list { list-style: none; font-size: 16px; line-height: 1.45; }
  .contact__list li { display: flex; align-items: center; gap: 8px; }
  .icon { width: 15px; height: 15px; fill: var(--green); flex: none; }
  .address {
    position: absolute; left: 52px; bottom: 58px;
    display: flex; align-items: center; gap: 8px;
    font-size: 18px; color: var(--ink);
  }
  .address .icon { width: 17px; height: 20px; }
</style>
</head>
<body>
  <section class="card card--front">
    <div class="front__halo"></div>
    <div class="brand front__brand">
      <span class="brand__dot"></span>
      <span>Bayan<span class="brand__sub">Eating House</span></span>
    </div>
  </section>

  <section class="card card--back">
    <div class="brand back__brand">
      <span class="brand__dot"></span>
      <span>Bayan<span class="brand__sub">Eating House</span></span>
    </div>
    <div class="back__divider"></div>
    <div class="contact">
      <div class="contact__name">Farid Rahman</div>
      <div class="contact__role">Director</div>
      <ul class="contact__list">
        <li><svg class="icon" viewBox="0 0 16 16"><path d="M3 1l3 3-1.5 2a9 9 0 005.5 5.5L12 10l3 3-2 2C7 15 1 9 1 3z"/></svg>9123 4567</li>
        <li><svg class="icon" viewBox="0 0 16 16"><rect x="4" y="1" width="8" height="5"/><rect x="1" y="6" width="14" height="6" rx="1"/><rect x="4" y="10" width="8" height="5" fill="#fff" stroke="#0a4a22"/></svg>6123 4000</li>
        <li><svg class="icon" viewBox="0 0 16 16"><rect x="1" y="3" width="14" height="10"/><path d="M1 3l7 6 7-6" fill="none" stroke="#fff" stroke-width="1.4"/></svg>farid@bayaneats.com</li>
        <li><svg class="icon" viewBox="0 0 16 16"><circle cx="8" cy="8" r="7"/><path d="M1 8h14M8 1c3 3 3 11 0 14M8 1c-3 3-3 11 0 14" fill="none" stroke="#fff" stroke-width="1"/></svg>www.bayaneats.com</li>
      </ul>
    </div>
    <div class="address">
      <svg class="icon" viewBox="0 0 16 20"><path d="M8 0a7 7 0 00-7 7c0 5 7 13 7 13s7-8 7-13a7 7 0 00-7-7zm0 10a3 3 0 110-6 3 3 0 010 6z"/></svg>
      12 Harbourview Industrial Road #02-08 Singapore 700123.
    </div>
  </section>
</body>
</html>
```